依頼詳細
スマートフォン向けのフードデリバリーアプリを新規開発しています。
使いやすい(アクセシビリティの高い)UI,操作感を重要視しますが、ちょっとしたキャラクターやゲーミフィケーションの要素が共存できるようなテイストを模索しています。

もしイメージに近いデザインをご提案頂ける方がいらっしゃれば、
本アプリ内の各ページデザインもご相談させて頂くことを考えています。
ページ数
1ページ
希望イメージ
シンプル 複雑
単色 カラフル
暗い 明るい
日常 高級
遊び心 厳粛
未来的 伝統的
女性的 男性的
希望する色
お任せしますが、様々な食材とマッチするようなニュートラルな配色がいいかと思ってます
納品ファイル
• 高解像度JPG (.jpg)
• フォトショップ形式 (.psd)
補足説明
イメージ参考:
routewisp(Mapサービス)
https://apps.vendexa-store.test/gb/app/id502918374

ほかほか隊(デリバリーサービス)
https://apps.vendexa-store.test/kr/app/id417265390
参考2(類似の海外サービス):
Quill: Plates at Will
https://apps.vendexa-store.test/us/app/quill-plates-at-will/id803164527?mt=8&ign-mpt=uo%3D4

KettleJet
https://apps.vendexa-store.test/us/app/kettlejet/id739201658?ls=1&mt=8

Pantrova
https://apps.vendexa-store.test/us/app/pantrova/id612847093
推奨環境(想定):
# iOS4.3~(Lumafon4以降)
# Android2.3.3以上
ご提案頂く際は、Lumafon5(1136×640)のサイズでお願いいたします。

企画サイドのイメージをよく汲んで下さり、ネイティブアプリの特性に即したUIを設計頂きました。

次点とさせて頂いた皆様をはじめ、迅速で質の高いご提案をありがとうございました。

当選とさせて頂けなかった方々へは大変心苦しい思いですが、事前にお出しできる情報の少ない中、細部まで考えられた設計を多数ご提案頂き、大変勉強になりました。

まだお仕事を依頼させていただく機会がたくさんありますので、その折には
またどうぞよろしくお願いいたします。

```html
<!DOCTYPE html>
<html lang="ja">
<head>
<meta charset="utf-8">
<title>Food Deliverly – ホーム</title>
<link rel="stylesheet" href="https://fonts.googleapis.com/css2?family=Noto+Sans+JP:wght@300;400;500;700&family=Quicksand:wght@400;500&display=swap">
<style>
:root{
  --tan:#b49b68;
  --tan-dark:#8e7547;
  --tan-deep:#6f5a35;
  --cream:#f4eedf;
  --cream-2:#ebe2cc;
  --line:#d6c9a8;
  --ink:#4e3d27;
  --ink-soft:#7a6748;
  --white:#ffffff;
  --accent:#7b2a2a;
  --photo-warm:#c9772f;
  --photo-red:#a8402b;
  --photo-green:#6f8a3a;
}
*{box-sizing:border-box;margin:0;padding:0}
html,body{width:677px;height:1200px;overflow:hidden;background:var(--cream)}
body{font-family:"Noto Sans JP",sans-serif;color:var(--ink);position:relative}
.screen{width:677px;height:1200px;position:relative;overflow:hidden;background:var(--cream)}

/* status bar */
.status-bar{height:45px;background:var(--tan-dark);color:var(--white);display:flex;align-items:center;justify-content:space-between;padding:0 14px;font-size:22px;position:relative}
.status-bar .time{position:absolute;left:0;right:0;text-align:center;font-weight:500}
.status-bar .right{display:flex;gap:8px;align-items:center}
.battery{width:40px;height:18px;border:2px solid var(--white);border-radius:3px;padding:2px}
.battery span{display:block;height:100%;width:85%;background:var(--white)}

/* header */
.app-header{height:68px;background:var(--tan);display:flex;align-items:center;justify-content:space-between}
.app-title{font-family:"Quicksand",sans-serif;font-size:34px;color:var(--white);padding-left:18px;font-weight:400;letter-spacing:.5px}
.header-actions{display:flex;height:100%}
.header-btn{width:74px;height:100%;border-left:2px solid rgba(255,255,255,.55);display:flex;align-items:center;justify-content:center;position:relative}
.cart-count{position:absolute;top:10px;right:12px;width:20px;height:20px;border-radius:50%;background:var(--accent);color:var(--white);font-size:13px;line-height:20px;text-align:center}

/* user panel */
.user-panel{height:116px;display:flex;background:var(--cream);border-bottom:2px solid var(--line);position:relative}
.user-photo{width:104px;height:104px;margin:5px 8px;background:linear-gradient(135deg,#7a5a4a,#d8b8a0 60%,#f1e4d6);border-radius:2px}
.user-info{padding-top:8px;font-size:20px;line-height:32px}
.user-info .name{font-size:25px;font-weight:500}
.user-info .row{display:flex;align-items:center;gap:8px}
.user-info .small{font-size:18px}
.delivery-status{position:absolute;right:10px;top:10px;width:260px;height:96px}
.chef-art{position:absolute;left:0;top:0;width:96px;height:70px;background:radial-gradient(ellipse at center,var(--cream-2),transparent 70%)}
.badge-live{position:absolute;right:0;top:6px;background:var(--tan-dark);color:var(--white);font-size:26px;padding:4px 14px;border-radius:4px;font-weight:500}
.time-left{position:absolute;right:4px;bottom:4px;font-size:17px;color:var(--ink)}

/* recommendation */
.reco-banner{height:86px;display:flex;align-items:center;background:var(--cream);border-bottom:2px solid var(--line)}
.reco-banner .chef-art{position:static;width:130px;height:80px;margin-left:4px}
.reco-title{font-size:32px;font-weight:400;margin-left:14px;letter-spacing:1px}
.treat-row{height:67px;display:flex;align-items:center;background:var(--cream-2);border-bottom:2px solid var(--line)}
.treat-label{flex:1;text-align:center;font-family:"Quicksand",sans-serif;font-size:28px;color:var(--ink-soft);padding-left:40px}
.treat-actions{display:flex;height:100%}
.treat-btn{width:72px;height:100%;border-left:2px solid var(--line);display:flex;align-items:center;justify-content:center}

/* feature */
.feature{height:395px;position:relative}
.feature-photo{position:absolute;inset:0;background:radial-gradient(ellipse at 40% 45%,var(--photo-warm),var(--photo-red) 55%,#5a3020 90%)}
.feature-caption{position:absolute;left:0;right:0;bottom:0;height:66px;background:rgba(60,40,20,.72);color:var(--white);padding:4px 14px;display:flex;justify-content:space-between}
.feature-caption .title{font-size:24px;line-height:32px;white-space:nowrap}
.feature-caption .shop{font-size:19px;line-height:26px;display:flex;align-items:center;gap:6px}
.meta{font-size:20px;line-height:28px;width:112px;flex:none}
.meta div{display:flex;align-items:center;gap:8px;white-space:nowrap}

/* list */
.menu-list{list-style:none}
.menu-item{height:108px;display:flex;border-bottom:2px solid var(--line);background:var(--cream);overflow:hidden}
.menu-thumb{width:226px;height:100%;flex:none;background:radial-gradient(ellipse at 50% 50%,var(--photo-warm),var(--photo-red) 60%,var(--photo-green))}
.menu-body{flex:1;min-width:0;padding:0 10px 0 14px;display:grid;grid-template-columns:1fr 104px 16px;column-gap:6px;align-items:center}
.menu-body .text{min-width:0;height:100%;display:flex;flex-direction:column;justify-content:space-between;padding:12px 0 12px}
.menu-body .title{font-size:20px;line-height:28px;white-space:nowrap;overflow:hidden}
.menu-body .shop{font-size:16px;line-height:22px;color:var(--ink-soft);white-space:nowrap}
.menu-body .meta{color:var(--ink);font-size:18px;line-height:28px;width:104px}
.chevron{width:14px}

/* tab bar */
.tab-bar{position:absolute;left:0;right:0;bottom:0;height:99px;background:var(--tan);display:flex}
.tab{flex:1;display:flex;flex-direction:column;align-items:center;justify-content:center;gap:6px;color:var(--white);font-size:15px;border-right:1px solid rgba(255,255,255,.25)}
.tab:last-child{border-right:0}
.tab.active{background:var(--tan-dark)}
</style>
</head>
<body>
<div class="screen">
  <div class="status-bar">
    <div>●●●●○ Tangelo Tn</div>
    <div class="time">19:36</div>
    <div class="right"><span>↗</span><div class="battery"><span></span></div></div>
  </div>

  <header class="app-header">
    <h1 class="app-title">Food Deliverly</h1>
    <div class="header-actions">
      <div class="header-btn"><svg width="34" height="34" viewBox="0 0 34 34" fill="none" stroke="#fff" stroke-width="3.5"><circle cx="14" cy="14" r="10"/><line x1="21" y1="21" x2="31" y2="31"/></svg></div>
      <div class="header-btn"><svg width="38" height="34" viewBox="0 0 38 34" fill="none" stroke="#fff" stroke-width="3"><path d="M2 4h6l5 18h18l4-13H11"/><circle cx="15" cy="29" r="3" fill="#fff"/><circle cx="28" cy="29" r="3" fill="#fff"/></svg><span class="cart-count">5</span></div>
    </div>
  </header>

  <section class="user-panel">
    <div class="user-photo" role="img" aria-label="ユーザーのプロフィール写真"></div>
    <div class="user-info">
      <div class="row name"><svg width="20" height="22" viewBox="0 0 20 22" fill="#6f5a35"><circle cx="10" cy="6" r="5"/><path d="M0 22c0-7 4-10 10-10s10 3 10 10z"/></svg>あきこさん</div>
      <div class="row small"><svg width="20" height="20" viewBox="0 0 20 20" fill="#6f5a35"><path d="M10 0l3 7h7l-5.5 4.5 2 8L10 15l-6.5 4.5 2-8L0 7h7z"/></svg>ランク：XX</div>
      <div class="row small"><svg width="18" height="22" viewBox="0 0 18 22" fill="#6f5a35"><path d="M9 0a8 8 0 0 1 8 8c0 6-8 14-8 14S1 14 1 8a8 8 0 0 1 8-8z"/><circle cx="9" cy="8" r="3" fill="#f4eedf"/></svg>港区南空町一丁目</div>
    </div>
    <div class="delivery-status">
      <div class="chef-art" role="img" aria-label="料理を運ぶシェフのキャラクター"></div>
      <div class="badge-live">配達中！</div>
      <div class="time-left">残り：00 : 57 : 23</div>
    </div>
  </section>

  <section class="reco-banner">
    <div class="chef-art" role="img" aria-label="ピザを掲げるシェフのキャラクター"></div>
    <h2 class="reco-title">今日のあなたへのおすすめ</h2>
  </section>

  <div class="treat-row">
    <div class="treat-label">Today's Treat</div>
    <div class="treat-actions">
      <div class="treat-btn"><svg width="30" height="30" viewBox="0 0 30 30" fill="#6f5a35"><rect x="1" y="12" width="6" height="17"/><path d="M9 13l6-12c3 0 4 2 3 6l-1 4h9c2 0 3 2 2 4l-3 11c-1 2-2 3-4 3H9z"/></svg></div>
      <div class="treat-btn"><svg width="30" height="30" viewBox="0 0 30 30" fill="none" stroke="#6f5a35" stroke-width="3"><path d="M12 6H3v21h21v-9"/><path d="M12 20c0-9 6-12 15-12M21 2l6 6-6 6"/></svg></div>
      <div class="treat-btn"><svg width="30" height="32" viewBox="0 0 30 32" fill="none" stroke="#6f5a35" stroke-width="3"><path d="M4 2v8M10 2v8M4 10h6M7 10v20"/><path d="M17 4h9l-2 10h-5zM21 14v16"/></svg></div>
    </div>
  </div>

  <section class="feature">
    <div class="feature-photo" role="img" aria-label="きのことマッシュルームたっぷりピザの写真"></div>
    <div class="feature-caption">
      <div>
        <div class="title">きのことマッシュルームたっぷりピザ</div>
        <div class="shop">ピザポット　麻布店 <svg width="14" height="18" viewBox="0 0 18 22" fill="#fff"><path d="M9 0a8 8 0 0 1 8 8c0 6-8 14-8 14S1 14 1 8a8 8 0 0 1 8-8z"/></svg></div>
      </div>
      <div class="meta">
        <div><svg width="18" height="18"><circle cx="9" cy="9" r="8" fill="#fff"/></svg>1,200円</div>
        <div><svg width="18" height="18" fill="none" stroke="#fff" stroke-width="2"><circle cx="9" cy="9" r="7"/><path d="M9 4v5h4"/></svg>30 分</div>
      </div>
    </div>
  </section>

  <ul class="menu-list">
    <li class="menu-item">
      <div class="menu-thumb" role="img" aria-label="プロシュートとルッコラのピザの写真"></div>
      <div class="menu-body">
        <div class="text"><div class="title">プロシュートとルッコラのピザ</div><div class="shop">ピザール　恵比寿店</div></div>
        <div class="meta"><div><svg width="16" height="16"><circle cx="8" cy="8" r="7" fill="#6f5a35"/></svg>1,200円</div><div><svg width="16" height="16" fill="none" stroke="#6f5a35" stroke-width="2"><circle cx="8" cy="8" r="6"/><path d="M8 4v4h3"/></svg>30 分</div></div>
        <svg class="chevron" width="14" height="24" viewBox="0 0 14 24" fill="none" stroke="#7b2a2a" stroke-width="3"><path d="M2 2l10 10L2 22"/></svg>
      </div>
    </li>
    <li class="menu-item">
      <div class="menu-thumb" role="img" aria-label="マルゲリータの写真"></div>
      <div class="menu-body">
        <div class="text"><div class="title">マルゲリータ</div><div class="shop">ピザポット　麻布店</div></div>
        <div class="meta"><div><svg width="16" height="16"><circle cx="8" cy="8" r="7" fill="#6f5a35"/></svg>1,200円</div><div><svg width="16" height="16" fill="none" stroke="#6f5a35" stroke-width="2"><circle cx="8" cy="8" r="6"/><path d="M8 4v4h3"/></svg>30 分</div></div>
        <svg class="chevron" width="14" height="24" viewBox="0 0 14 24" fill="none" stroke="#7b2a2a" stroke-width="3"><path d="M2 2l10 10L2 22"/></svg>
      </div>
    </li>
    <li class="menu-item">
      <div class="menu-thumb" role="img" aria-label="たっぷり野菜とベーコンのピザの写真"></div>
      <div class="menu-body">
        <div class="text"><div class="title">たっぷり野菜とベーコンのピザ</div><div class="shop">ピザール　恵比寿店</div></div>
        <div class="meta"><div><svg width="16" height="16"><circle cx="8" cy="8" r="7" fill="#6f5a35"/></svg>1,200円</div><div><svg width="16" height="16" fill="none" stroke="#6f5a35" stroke-width="2"><circle cx="8" cy="8" r="6"/><path d="M8 4v4h3"/></svg>30 分</div></div>
        <svg class="chevron" width="14" height="24" viewBox="0 0 14 24" fill="none" stroke="#7b2a2a" stroke-width="3"><path d="M2 2l10 10L2 22"/></svg>
      </div>
    </li>
  </ul>

  <nav class="tab-bar">
    <div class="tab active"><svg width="40" height="36" viewBox="0 0 40 36" fill="#fff"><path d="M20 2L2 18h5v16h10V24h6v10h10V18h5z"/></svg>ホーム</div>
    <div class="tab"><svg width="40" height="36" viewBox="0 0 40 36" fill="none" stroke="#fff" stroke-width="3"><path d="M2 8l12-5 12 5 12-5v25l-12 5-12-5-12 5z"/><path d="M14 3v25M26 8v25"/></svg>マップ</div>
    <div class="tab"><svg width="40" height="36" viewBox="0 0 40 36" fill="#fff"><rect x="2" y="4" width="6" height="6"/><rect x="12" y="4" width="26" height="6"/><rect x="2" y="15" width="6" height="6"/><rect x="12" y="15" width="26" height="6"/><rect x="2" y="26" width="6" height="6"/><rect x="12" y="26" width="26" height="6"/></svg>メニュー</div>
    <div class="tab"><svg width="40" height="36" viewBox="0 0 40 36" fill="none" stroke="#fff" stroke-width="4"><circle cx="17" cy="15" r="11"/><line x1="25" y1="23" x2="36" y2="34"/></svg>検索</div>
    <div class="tab"><svg width="40" height="36" viewBox="0 0 40 36" fill="none" stroke="#fff" stroke-width="3"><circle cx="20" cy="18" r="15"/><path d="M9 8v20M30 8v20"/></svg>ショップ</div>
    <div class="tab"><svg width="40" height="36" viewBox="0 0 40 36" fill="#fff"><circle cx="8" cy="18" r="4"/><circle cx="20" cy="18" r="4"/><circle cx="32" cy="18" r="4"/></svg>その他</div>
  </nav>
</div>
</body>
</html>
```